UX revamp for crypto platform mobile app

re-design the assets of a mobile app to give them a sleek, current and modern feel see reference below.
The current app has 3 main menus with subfunctions:
Wallet: Send - Receive - Top-up with shortcut to other main menus
Talents: User can support talent and see his support
Rewards: User can purchase rewards from Talents - Clubs - Vexmint

Target Market(s)

Youth fans of sports and entertainment

Industry/Entity Type

Blockchain

Colors

Designer to choose colors to be used in the design.

Requirements
Must have
• Modern - sleek - stylish - current trends design
Nice to have
• Need to be clean design
Should not have
• too dark and heavy

```html
<!DOCTYPE html>
<html lang="en">
<head>
<meta charset="utf-8">
<title>Vexmint Wallet UI Assets</title>
<link href="https://fonts.googleapis.com/css2?family=Montserrat:wght@500;600&display=swap" rel="stylesheet">
<style>
  :root {
    --orange: #f5883a;
    --blue: #2f9ff0;
    --green: #22b83a;
    --panel: #f7f7f7;
    --page: #ffffff;
    --white: #ffffff;
  }
  * { box-sizing: border-box; margin: 0; padding: 0; }
  html, body { width: 1200px; height: 880px; overflow: hidden; background: var(--page); }
  .canvas { position: relative; width: 1200px; height: 880px; font-family: 'Montserrat', sans-serif; }
  .panel { position: absolute; left: 10px; top: 11px; width: 1180px; height: 856px; background: var(--panel); }

  .btn {
    position: absolute; width: 336px; height: 65px;
    border: 3px solid currentColor; border-radius: 6px;
    display: flex; align-items: center; justify-content: center;
    font-weight: 600; font-size: 18px; letter-spacing: 0.14em;
    white-space: nowrap;
  }
  .btn--orange { color: var(--orange); }
  .btn--blue { color: var(--blue); }
  .btn--green { color: var(--green); }
  .btn--large { font-size: 22px; letter-spacing: 0.16em; }
  .btn__icon { position: absolute; left: 22px; top: 50%; width: 26px; height: 26px; transform: translateY(-50%); }
  .btn__icon svg { width: 100%; height: 100%; fill: none; stroke: currentColor; stroke-width: 1.5; stroke-linecap: round; stroke-linejoin: round; }
  .btn__label { margin-right: -0.14em; }

  .menu-badge {
    position: absolute; width: 72px; height: 72px; margin: -36px 0 0 -36px; top: 500px;
    border: 3px solid var(--blue); border-radius: 50%; color: var(--blue);
    display: flex; flex-direction: column; align-items: center; justify-content: center;
  }
  .menu-badge svg { width: 28px; height: 28px; fill: none; stroke: currentColor; stroke-width: 1.3; stroke-linecap: round; stroke-linejoin: round; margin-top: 4px; }
  .menu-badge span { font-size: 8px; letter-spacing: 0.1em; margin-top: 3px; font-weight: 500; }

  .icon-dot {
    position: absolute; width: 52px; height: 52px; margin: -26px 0 0 -26px;
    border-radius: 50%; background: var(--blue); color: var(--white);
    display: flex; align-items: center; justify-content: center;
  }
  .icon-dot svg { width: 32px; height: 32px; fill: none; stroke: currentColor; stroke-width: 1.4; stroke-linecap: round; stroke-linejoin: round; }
</style>
</head>
<body>
<div class="canvas">
  <div class="panel"></div>

  <!-- Left column: auth buttons -->
  <div class="btn btn--orange btn--large" style="left:212px;top:179px">
    <span class="btn__icon"><svg viewBox="0 0 24 24"><rect x="6" y="10" width="12" height="11" rx="2"/><path d="M8.5 10V7a3.5 3.5 0 0 1 7 0v3"/><circle cx="12" cy="15.5" r="1.3"/></svg></span>
    <span class="btn__label">LOGIN</span>
  </div>
  <div class="btn btn--blue btn--large" style="left:212px;top:264px">
    <span class="btn__icon"><svg viewBox="0 0 24 24"><path d="M9 4h10v16H9"/><path d="M3 12h12M11 8l4 4-4 4"/></svg></span>
    <span class="btn__label">REGISTER</span>
  </div>
  <div class="btn btn--blue btn--large" style="left:212px;top:348px">
    <span class="btn__icon"><svg viewBox="0 0 24 24"><path d="M13 5H5v15h15v-8"/><path d="M18 3l3 3-9 9-4 1 1-4z"/></svg></span>
    <span class="btn__label">SIGN UP</span>
  </div>

  <!-- Main menu badges -->
  <div class="menu-badge" style="left:209px">
    <svg viewBox="0 0 24 24"><path d="M22 3L2 11l7 3 10-8-8 9v6l3-4 4 3z"/></svg><span>SEND</span>
  </div>
  <div class="menu-badge" style="left:294px">
    <svg viewBox="0 0 24 24"><circle cx="10" cy="7" r="4"/><path d="M3 20c0-4 3-7 7-7 1.5 0 2.5.3 3.5.8"/><path d="M18 13l1.2 2.4 2.6.4-1.9 1.8.5 2.6-2.4-1.3-2.4 1.3.5-2.6-1.9-1.8 2.6-.4z"/></svg><span>TALENT</span>
  </div>
  <div class="menu-badge" style="left:380px">
    <svg viewBox="0 0 24 24"><rect x="3" y="3" width="7" height="7"/><rect x="14" y="3" width="7" height="7"/><rect x="3" y="14" width="7" height="7"/><rect x="5.5" y="5.5" width="2" height="2"/><rect x="16.5" y="5.5" width="2" height="2"/><rect x="5.5" y="16.5" width="2" height="2"/><path d="M14 14h3v3h-3zM17 17h4v4h-4z"/></svg><span>RECEIVE</span>
  </div>
  <div class="menu-badge" style="left:466px">
    <svg viewBox="0 0 24 24"><rect x="7" y="2" width="10" height="20" rx="1.5"/><path d="M7 5h10M7 18h10"/><circle cx="12" cy="11.5" r="2.5"/><circle cx="12" cy="20" r=".5"/></svg><span>TOP UP</span>
  </div>
  <div class="menu-badge" style="left:551px">
    <svg viewBox="0 0 24 24"><circle cx="12" cy="9" r="6"/><circle cx="12" cy="9" r="3.5"/><path d="M8 14l-3 7 3-1 2 2 2-5 2 5 2-2 3 1-3-7"/></svg><span>REWARD</span>
  </div>

  <!-- Icon set, row 1 -->
  <div class="icon-dot" style="left:257px;top:613px"><svg viewBox="0 0 32 32"><circle cx="16" cy="16" r="11"/><path d="M11 16l3.5 3.5L21 13"/></svg></div>
  <div class="icon-dot" style="left:319px;top:613px"><svg viewBox="0 0 32 32"><circle cx="16" cy="16" r="11"/><circle cx="16" cy="16" r="8"/></svg></div>
  <div class="icon-dot" style="left:381px;top:613px"><svg viewBox="0 0 32 32"><path d="M16 3l3.8 8 8.7 1-6.4 6 1.7 8.7L16 22.4l-7.8 4.3 1.7-8.7-6.4-6 8.7-1z"/><path d="M18 13.5c-.5-.8-1.2-1-2-1-1.2 0-2 .7-2 1.5 0 2 4 1.2 4 3.3 0 .9-.9 1.6-2 1.6-.9 0-1.6-.3-2.1-1M16 11v1.5M16 18.9v1.4"/></svg></div>
  <div class="icon-dot" style="left:443px;top:613px"><svg viewBox="0 0 32 32"><rect x="4" y="9" width="24" height="17" rx="2"/><path d="M12 9V6h8v3M4 16h24"/><rect x="14.5" y="14.5" width="3" height="4"/></svg></div>
  <div class="icon-dot" style="left:505px;top:613px"><svg viewBox="0 0 32 32"><circle cx="15" cy="9" r="4.5"/><path d="M4 20c3-2 6-2 9 0h6c1.5 0 1.5 2 0 2h-6"/><path d="M4 24c4 2 8 2 12 1l10-3M22 18h6M25 18v6"/></svg></div>

  <!-- Icon set, row 2 -->
  <div class="icon-dot" style="left:226px;top:676px"><svg viewBox="0 0 32 32"><circle cx="16" cy="10" r="4"/><circle cx="9" cy="11" r="3.5"/><circle cx="23" cy="11" r="3.5"/><path d="M9 26v-4c0-4 3-7 7-7s7 3 7 7v4z"/><path d="M9 17c-3 0-5 2-5 5v3h4M23 17c3 0 5 2 5 5v3h-4"/></svg></div>
  <div class="icon-dot" style="left:288px;top:676px"><svg viewBox="0 0 32 32"><rect x="4" y="9" width="24" height="16" rx="2"/><path d="M4 14h24M8 20h6M8 22h4"/><circle cx="22" cy="20" r="1.5"/><circle cx="14" cy="7" r="2"/><circle cx="18" cy="7" r="2"/></svg></div>
  <div class="icon-dot" style="left:350px;top:676px"><svg viewBox="0 0 32 32"><circle cx="13" cy="10" r="5"/><path d="M4 27c0-5.5 4-9 9-9 2 0 3.5.5 5 1.3"/><path d="M23 17l1.6 3.2 3.4.5-2.5 2.4.6 3.4-3.1-1.7-3.1 1.7.6-3.4-2.5-2.4 3.4-.5z"/></svg></div>
  <div class="icon-dot" style="left:412px;top:676px"><svg viewBox="0 0 32 32"><path d="M3 6h4l3 14h15l2-10H9"/><path d="M10 20l-1 3h17"/><circle cx="12" cy="26" r="1.5"/><circle cx="22" cy="26" r="1.5"/></svg></div>
  <div class="icon-dot" style="left:474px;top:676px"><svg viewBox="0 0 32 32"><circle cx="16" cy="12" r="7.5"/><circle cx="16" cy="12" r="4.5"/><path d="M11 18l-4 9 4-1 2 3 3-7 3 7 2-3 4 1-4-9"/></svg></div>
  <div class="icon-dot" style="left:536px;top:676px"><svg viewBox="0 0 32 32"><path d="M18 6H6v21h12"/><path d="M14 16.5h14M23 11.5l5 5-5 5"/></svg></div>

  <!-- Right column: action buttons -->
  <div class="btn btn--orange" style="left:690px;top:179px">
    <span class="btn__icon"><svg viewBox="0 0 24 24"><circle cx="12" cy="12" r="9.5"/><path d="M8 12l3 3 5-6"/></svg></span>
    <span class="btn__label">CONFIRM</span>
  </div>
  <div class="btn btn--orange" style="left:690px;top:258px">
    <span class="btn__icon"><svg viewBox="0 0 24 24"><path d="M15 3l5 4.5-5 4.5V9.5c-4 0-7 1.5-8.5 5 .5-5 3.5-8 8.5-8.5z"/><path d="M18 14v6H3V9h3"/></svg></span>
    <span class="btn__label">IMPORT</span>
  </div>
  <div class="btn btn--orange" style="left:690px;top:334px">
    <span class="btn__icon"><svg viewBox="0 0 24 24"><path d="M22 3L2 11l7 3 10-8-8 9v6l3-4 4 3z"/></svg></span>
    <span class="btn__label">SEND</span>
  </div>
  <div class="btn btn--orange" style="left:690px;top:411px">
    <span class="btn__icon"><svg viewBox="0 0 24 24"><circle cx="12" cy="4" r="1.8"/><circle cx="4" cy="18" r="1.8"/><circle cx="20" cy="18" r="1.8"/><path d="M9.8 4.5A8.5 8.5 0 0 0 3.6 15.8M14.2 4.5a8.5 8.5 0 0 1 6.2 11.3M6 19.5a8.5 8.5 0 0 0 12 0"/></svg></span>
    <span class="btn__label">SHARE</span>
  </div>
  <div class="btn btn--blue" style="left:690px;top:486px">
    <span class="btn__icon"><svg viewBox="0 0 24 24"><path d="M13 5H4v16h16v-8"/><path d="M18 3l3 3-9 9-4 1 1-4z"/></svg></span>
    <span class="btn__label">CREATE WALLET</span>
  </div>
  <div class="btn btn--orange" style="left:690px;top:562px">
    <span class="btn__icon"><svg viewBox="0 0 24 24"><path d="M10 3h10v18H10"/><path d="M22 12H4M8 8l-4 4 4 4"/></svg></span>
    <span class="btn__label">LOGOUT</span>
  </div>
  <div class="btn btn--green" style="left:690px;top:637px">
    <span class="btn__icon"><svg viewBox="0 0 24 24" style="stroke-width:2.2"><path d="M20 11a8 8 0 0 0-14.5-4.5M4 13a8 8 0 0 0 14.5 4.5"/><path d="M5 2.5v4.5h4.5M19 21.5V17h-4.5"/></svg></span>
    <span class="btn__label">RECOVER WALLET</span>
  </div>
</div>
</body>
</html>
```